Selling my Home Flyer

I need a flyer/brochure for a house listing I am putting together. I will put all of the information together for you to include in the flyer. This will only be a front and back flyer. No extra pages and no staples will be seen. This will be printed by a large office copier, not a professional copier on standard paper. Therefore no crazy dark backgrounds with lots of bleeding colors. Pictures that I want need for sure in there are Aerial with outline, Front from left, and one of the ones showing the large yard. I included a couple sample designs that I don't hate. But feel free to get creative. I will need this on a quick turnaround and I will make comments quickly as well, so submit ASAP.

Target Market(s)

People that will by my house.

Industry/Entity Type

Real Estate Agent

Font styles to use
Serif
Sans Serif

Colors

Designer to choose colors to be used in the design.

Requirements
Must have
• The pictures I mentioned above. And the price and SF and address! I forgot to tell you the address. It is 4817 Birchwell Lane, Palm Beach Gardens, FL 33410.
Should not have
• Anarchy. I don't want it to look too crazy. Should be pretty straight forward.

```html
<!DOCTYPE html>
<html lang="en">
<head>
<meta charset="utf-8">
<title>Listing Flyer – 4817 Birchwell Lane</title>
<link rel="stylesheet" href="https://fonts.googleapis.com/css2?family=Open+Sans:ital,wght@0,400;0,600;0,700;1,400;1,600&family=Arimo:ital,wght@0,400;0,700;1,400;1,700&family=PT+Serif:wght@700&display=swap">
<style>
:root{
  --bg:#dcdcdc;
  --paper:#f1f1f1;
  --green:#27a866;
  --green-dark:#1c7d4b;
  --yellow:#dfdb2c;
  --purple:#5b2a86;
  --red:#d91f26;
  --gold:#ffe23a;
  --ink:#1d1d1d;
  --teal:#1aa39a;
  --white:#ffffff;
}
*{box-sizing:border-box;margin:0;padding:0}
html,body{width:1200px;height:1000px;overflow:hidden;background:var(--bg)}
body{position:relative;font-family:"Open Sans",sans-serif;color:var(--ink)}
.page{position:absolute;top:140px;width:512px;height:725px;background:var(--paper);overflow:hidden}
.page--front{left:47px}
.page--back{left:648px}
.photo{position:absolute}
.hero-front{left:0;top:36px;width:512px;height:294px;background:linear-gradient(180deg,#7fb5e3 0%,#b9d0b0 35%,#5f8f47 70%,#4f8a2f 100%)}
.sale-banner{position:absolute;left:37px;top:0;width:129px;height:174px;background:var(--yellow);clip-path:polygon(0 0,100% 0,100% 90%,50% 100%,0 90%);padding:46px 4px 0 6px}
.sale-banner h1{font-family:"Arimo",sans-serif;font-weight:700;font-size:24px;color:var(--purple);line-height:1;white-space:nowrap}
.sale-banner p{margin-top:18px;padding-left:4px;font-family:"Arimo",sans-serif;font-weight:700;font-size:11.5px;line-height:15.3px;color:var(--purple);white-space:nowrap}
.price-badge{position:absolute;left:272px;top:255px;width:124px;height:124px;z-index:5}
.price-badge svg{position:absolute;inset:0}
.price-text{position:absolute;inset:0;display:flex;flex-direction:column;align-items:center;justify-content:center;text-align:center}
.price-text .lead{font-size:14px;color:var(--white);font-weight:600;margin-top:-4px}
.price-text .amount{font-family:"PT Serif",serif;font-weight:700;font-size:21px;color:var(--gold);line-height:1.1}
.location{position:absolute;left:26px;top:338px;width:147px;height:106px}
.location svg{position:absolute;inset:0}
.location-text{position:absolute;left:9px;top:31px;color:var(--white);font-family:"Arimo",sans-serif;font-style:italic;white-space:nowrap}
.location-text strong{display:block;font-size:13px;font-weight:700;margin-bottom:4px}
.location-text span{display:block;font-size:13.5px;line-height:14.5px}
.stats{position:absolute;left:26px;top:454px;width:147px;height:104px;background:var(--yellow);font-family:"Arimo",sans-serif;text-align:center;padding-top:10px}
.stats p{font-size:15px;line-height:28.5px}
.stats small{font-size:11px;text-transform:uppercase}
.thumb{width:146px;height:106px}
.thumb-a{left:183px;top:338px;background:linear-gradient(160deg,#e9e4dc,#b79e86 60%,#6e5140)}
.thumb-b{left:340px;top:338px;background:linear-gradient(160deg,#f2efe9,#cfc7bb 60%,#8f8275)}
.thumb-c{left:183px;top:454px;height:104px;background:linear-gradient(160deg,#ede5d8,#a78a68 60%,#5a4634)}
.thumb-d{left:340px;top:454px;height:104px;background:linear-gradient(160deg,#f6f4f1,#dcd6cf 60%,#a59a8f)}
.blurb{position:absolute;left:26px;top:570px;width:466px;font-family:"Arimo",sans-serif;font-style:italic;font-size:12px;line-height:14.5px}
.blurb p:first-child{text-align:justify}
.blurb p+p{margin-top:13px}
.contact-bar{position:absolute;left:0;top:635px;width:512px;height:65px;background:var(--green);color:var(--white);z-index:4}
.contact-name{position:absolute;left:27px;top:12px;font-size:15px;line-height:19px}
.contact-name em{font-style:italic;display:block}
.contact-name strong{font-weight:700;display:block}
.contact-arrow{position:absolute;left:127px;top:12px}
.contact-phone{position:absolute;left:161px;top:18px;font-size:21px;letter-spacing:.3px}
.contact-divider{position:absolute;left:320px;top:12px;width:1px;height:42px;background:rgba(255,255,255,.55)}
.contact-email{position:absolute;left:336px;top:25px;font-size:11px}
.page--back .contact-bar{top:634px}
.hero-back{left:0;top:43px;width:512px;height:287px;background:linear-gradient(170deg,#c9a27a 0%,#8c8a86 30%,#6c6a66 55%,#3c6a2c 80%,#2f5a22 100%)}
.features-title{position:absolute;left:20px;top:343px;width:218px;height:28px}
.features-title svg{position:absolute;inset:0}
.features-title h2{position:absolute;left:33px;top:1px;font-family:"Arimo",sans-serif;font-weight:700;font-style:italic;font-size:21px;color:var(--white)}
.features{position:absolute;left:45px;top:379px;width:197px;list-style:none;font-size:11.5px;font-weight:600;line-height:14.5px}
.features li{position:relative;padding-left:14px;margin-bottom:7px}
.features li::before{content:"";position:absolute;left:0;top:4px;width:7px;height:7px;border-radius:50%;background:var(--teal)}
.aerial{left:260px;top:342px;width:223px;height:146px;background:linear-gradient(135deg,#3f6f2c,#6c8f4a 50%,#b6a48c)}
.pool{left:260px;top:500px;width:223px;height:133px;background:linear-gradient(180deg,#b87b4e 0%,#c9c2b4 40%,#2fb3d3 75%,#1a86b0 100%)}
</style>
</head>
<body>

<section class="page page--front">
  <div class="photo hero-front" role="img" aria-label="Front exterior of the two-storey Mediterranean pool home with palms and lawn, viewed from the left"></div>

  <div class="sale-banner">
    <h1>FOR SALE</h1>
    <p>POOL HOME ON<br>COVETED CORNER<br>LOT WITH<br>OVERSIZED YARD.</p>
  </div>

  <div class="location">
    <svg viewBox="0 0 147 106" aria-hidden="true"><polygon fill="var(--green)" points="0,18 74,0 147,18 147,106 0,106"/></svg>
    <div class="location-text">
      <strong>Location:</strong>
      <span>4817 Birchwell Lane,</span>
      <span>Palm Beach Gardens,</span>
      <span>FL 33410</span>
    </div>
  </div>

  <div class="photo thumb thumb-a" role="img" aria-label="Primary bedroom with wooden bed and ceiling fan"></div>
  <div class="photo thumb thumb-b" role="img" aria-label="Open living room and kitchen"></div>

  <div class="stats">
    <p>2,307 SF <small>of size</small></p>
    <p>3 <small>bedrooms</small></p>
    <p>2 ½ <small>bathrooms</small></p>
  </div>

  <div class="photo thumb thumb-c" role="img" aria-label="Dining room with chandelier and hutch"></div>
  <div class="photo thumb thumb-d" role="img" aria-label="Bright nursery bedroom with crib"></div>

  <div class="price-badge">
    <svg viewBox="0 0 124 124" aria-hidden="true">
      <defs>
        <radialGradient id="badgeFill" cx="50%" cy="40%" r="60%">
          <stop offset="0" stop-color="#f04a3f"/>
          <stop offset="1" stop-color="#c4161c"/>
        </radialGradient>
      </defs>
      <polygon fill="url(#badgeFill)" points="62,2 70,11 81,5 86,16 98,14 99,26 111,28 108,40 119,46 112,55 121,62 112,69 119,78 108,84 111,96 99,98 98,110 86,108 81,119 70,113 62,122 54,113 43,119 38,108 26,110 25,98 13,96 16,84 5,78 12,69 3,62 12,55 5,46 16,40 13,28 25,26 26,14 38,16 43,5 54,11"/>
    </svg>
    <div class="price-text">
      <span class="lead">Offered at</span>
      <span class="amount">$570,000</span>
    </div>
  </div>

  <div class="blurb">
    <p>This impressive home boasts one of the largest yards in Palm Beach Gardens' most family friendly community, Willowmere.</p>
    <p>Enjoy the ultimate Florida lifestyle with a beautiful pool &amp; expanded patio areas.</p>
  </div>

  <footer class="contact-bar">
    <div class="contact-name"><em>Contact</em><strong>Dana Harlow</strong></div>
    <svg class="contact-arrow" width="16" height="42" viewBox="0 0 16 42" aria-hidden="true"><polygon fill="var(--white)" points="0,0 16,21 0,42"/></svg>
    <div class="contact-phone">561-555-0147</div>
    <div class="contact-divider"></div>
    <div class="contact-email">dana@harlowhomes.com</div>
  </footer>
</section>

<section class="page page--back">
  <div class="photo hero-back" role="img" aria-label="Back patio with grill and dining table beside the large lawn at sunset"></div>

  <div class="features-title">
    <svg viewBox="0 0 218 34" aria-hidden="true">
      <polygon fill="var(--green-dark)" points="0,26 12,26 12,34"/>
      <polygon fill="var(--green)" points="10,0 218,0 208,26 0,26"/>
    </svg>
    <h2>More Features</h2>
  </div>

  <ul class="features">
    <li>Perfect for entertaining.</li>
    <li>Upgraded features throughout.</li>
    <li>Custom wood and ship lap details in all bathrooms and loft.</li>
    <li>New dark wood laminate flooring upstairs.</li>
    <li>New high-efficiency A/C units with smart thermostats.</li>
    <li>New pool pump and new heater controlled from your phone! Crown molding throughout.</li>
    <li>Walk-in closets.</li>
    <li>Quiet &amp; private cul-de-sac.</li>
  </ul>

  <div class="photo aerial" role="img" aria-label="Aerial view of the lot with the property line outlined"></div>
  <div class="photo pool" role="img" aria-label="Screened pool and patio at dusk"></div>

  <footer class="contact-bar">
    <div class="contact-name"><em>Contact</em><strong>Dana Harlow</strong></div>
    <svg class="contact-arrow" width="16" height="42" viewBox="0 0 16 42" aria-hidden="true"><polygon fill="var(--white)" points="0,0 16,21 0,42"/></svg>
    <div class="contact-phone">561-555-0147</div>
    <div class="contact-divider"></div>
    <div class="contact-email">dana@harlowhomes.com</div>
  </footer>
</section>

</body>
</html>
```